Cedarfield Supply METAL business card

A metal business card design. Attached are older designs for a reference, but we want a NEW design, not the same as in the past. See the 2 examples just posted. We would like some cut out in the design. Possibly the pine cone or the pine tree branch (see image IMG_0).

Target Market(s)

Home and Gardern

Industry/Entity Type

Landscape

Contact Information for Business Card

Logo, website, address, name, phone numbers

```html
<!DOCTYPE html>
<html lang="en">
<head>
<meta charset="utf-8">
<title>Cedarfield Supply – Metal Business Card</title>
<link href="https://fonts.googleapis.com/css2?family=Poppins:wght@400;600;800&family=Yellowtail&display=swap" rel="stylesheet">
<style>
  :root {
    --backdrop: #2a2a2a;
    --black-metal-1: #1c1c1c;
    --black-metal-2: #050505;
    --silver-1: #f4f4f4;
    --silver-2: #c9c9c9;
    --orange: #f0901e;
    --ink: #2d2d2d;
    --cone-light: #ffffff;
    --cone-mid: #d6d6d6;
    --cone-dark-1: #151515;
    --cone-dark-2: #000000;
  }
  * { box-sizing: border-box; margin: 0; padding: 0; }
  html, body { width: 1200px; height: 866px; overflow: hidden; }
  body {
    background: var(--backdrop);
    display: flex;
    align-items: center;
    justify-content: center;
    gap: 40px;
    font-family: "Poppins", sans-serif;
  }
  .card {
    position: relative;
    width: 540px;
    height: 309px;
    border-radius: 4px;
    overflow: hidden;
    box-shadow: 0 14px 30px rgba(0,0,0,.55);
  }
  .card--front {
    background: linear-gradient(135deg, var(--black-metal-1), var(--black-metal-2));
  }
  .card--back {
    background: linear-gradient(120deg, var(--silver-2) 0%, var(--silver-1) 45%, var(--silver-2) 100%);
  }
  .cone-art {
    position: absolute;
    right: -40px;
    top: 20px;
    width: 300px;
    height: 320px;
    border-radius: 48% 52% 40% 44%;
  }
  .card--front .cone-art {
    background: radial-gradient(circle at 40% 40%, var(--cone-dark-1), var(--cone-dark-2) 75%);
  }
  .card--back .cone-art {
    background: radial-gradient(circle at 40% 35%, var(--cone-light) 30%, var(--cone-mid) 80%);
  }
  .brand {
    position: absolute;
    left: 44px;
    top: 50%;
    transform: translateY(-50%);
    display: flex;
    align-items: center;
    gap: 14px;
  }
  .brand__mark {
    width: 34px;
    height: 34px;
    border-radius: 50%;
    background: var(--orange);
  }
  .brand__name {
    color: var(--orange);
    font-weight: 800;
    font-size: 30px;
    line-height: 1.05;
  }
  .contact {
    position: absolute;
    left: 40px;
    top: 44px;
    color: var(--ink);
  }
  .contact__name {
    font-family: "Yellowtail", cursive;
    color: var(--orange);
    font-size: 30px;
    line-height: 1;
  }
  .rule {
    width: 36px;
    height: 2px;
    background: var(--orange);
    margin: 10px 0;
  }
  .contact__line {
    display: flex;
    align-items: center;
    gap: 7px;
    font-size: 13px;
    line-height: 1.45;
  }
  .contact__line svg { width: 11px; height: 11px; flex: none; }
  .contact__address { font-size: 13px; line-height: 1.45; }
  .social { display: flex; gap: 8px; align-items: center; }
  .social__dot { width: 11px; height: 11px; background: var(--orange); }
  .social__dot--round { border-radius: 50%; }
</style>
</head>
<body>
  <section class="card card--front">
    <div class="cone-art" role="img" aria-label="Embossed pine cone illustration in black on black"></div>
    <div class="brand">
      <span class="brand__mark"></span>
      <span class="brand__name">Cedarfield<br>Supply</span>
    </div>
  </section>

  <section class="card card--back">
    <div class="cone-art" role="img" aria-label="Embossed white pine cone and branch illustration"></div>
    <div class="contact">
      <p class="contact__name">Dalton Meyers</p>
      <div class="rule"></div>
      <p class="contact__line">
        <svg viewBox="0 0 24 24"><path fill="#f0901e" d="M6.6 10.8a15 15 0 0 0 6.6 6.6l2.2-2.2a1 1 0 0 1 1-.25 11 11 0 0 0 3.6.6 1 1 0 0 1 1 1V20a1 1 0 0 1-1 1A17 17 0 0 1 3 4a1 1 0 0 1 1-1h3.5a1 1 0 0 1 1 1c0 1.25.2 2.45.6 3.6a1 1 0 0 1-.25 1z"/></svg>
        888.555.0142
      </p>
      <p class="contact__line">
        <svg viewBox="0 0 24 24"><path fill="#f0901e" d="M6.6 10.8a15 15 0 0 0 6.6 6.6l2.2-2.2a1 1 0 0 1 1-.25 11 11 0 0 0 3.6.6 1 1 0 0 1 1 1V20a1 1 0 0 1-1 1A17 17 0 0 1 3 4a1 1 0 0 1 1-1h3.5a1 1 0 0 1 1 1c0 1.25.2 2.45.6 3.6a1 1 0 0 1-.25 1z"/></svg>
        601.555.0187
      </p>
      <p class="contact__line">
        <svg viewBox="0 0 24 24"><circle cx="12" cy="12" r="10" fill="none" stroke="#f0901e" stroke-width="3"/><path d="M2 12h20M12 2c3 3 3 17 0 20M12 2c-3 3-3 17 0 20" fill="none" stroke="#f0901e" stroke-width="2"/></svg>
        cedarfieldsupply.com
      </p>
      <div class="rule"></div>
      <p class="contact__address">240 Birch Hollow Road<br>Fairview, MS 39000</p>
      <div class="rule"></div>
      <div class="social">
        <span class="social__dot social__dot--round"></span>
        <span class="social__dot"></span>
      </div>
    </div>
  </section>
</body>
</html>
```